Your complete Gardening and lawn maintenance, Horticultural care. (to be on card)
We are looking at using a logo of a tree, with a recycling emblem circling the tree. The colors of choice, are burnt oranges and olive greens. Presented; simple to the eye, yet catchy to the clients in a eco-friendly way. We have uploaded a design for you to look at just to give a rough idea, you can use that or create your own ideas or play around with a mixture.

Target Market(s)

Home owners, businesses, real estates.

Industry/Entity Type

Recycling

Contact Information for Business Card

Name: Derek Ostrowe
Phone: 0421583906
Email: bramblewoodyards@mailnest.net

Logo Text

Bramble-Wood Yards

Logo styles of interest
Emblem Logo
Pictorial/Combination Logo
Abstract Logo
Requirements
Must have
• Business name: Bramble-Wood Yards
and slogan : Your complete Gardening and lawn maintenance, Horticultural care

```html
<!DOCTYPE html>
<html lang="en">
<head>
<meta charset="utf-8">
<title>Bramble-Wood Yards – Business Card</title>
<link href="https://fonts.googleapis.com/css2?family=Roboto:wght@300;400;700;900&display=swap" rel="stylesheet">
<style>
  :root {
    --page-bg: #d9d7d2;
    --card-cream: #ece8da;
    --olive-bright: #a9a41e;
    --olive-dark: #54540f;
    --olive-mid: #8b8a2c;
    --band-text: #cdc63f;
    --ink: #3d3a1c;
  }
  * { margin: 0; padding: 0; box-sizing: border-box; }
  html, body {
    width: 1200px;
    height: 1000px;
    overflow: hidden;
    background: var(--page-bg);
    font-family: "Roboto", Arial, sans-serif;
  }
  .card {
    position: absolute;
    left: 150px;
    top: 243px;
    width: 900px;
    height: 514px;
    background: var(--card-cream);
    box-shadow: 0 10px 30px rgba(0,0,0,0.18);
  }
  .brand {
    position: absolute;
    left: 70px;
    top: 110px;
    display: flex;
    align-items: center;
    gap: 24px;
  }
  .brand-dot {
    width: 64px;
    height: 64px;
    border-radius: 50%;
    background: var(--olive-mid);
  }
  .brand-name {
    font-weight: 900;
    font-size: 62px;
    letter-spacing: 1px;
    color: var(--olive-bright);
    text-transform: uppercase;
    line-height: 1;
  }
  .slogan-band {
    position: absolute;
    left: 0;
    top: 268px;
    width: 100%;
    height: 52px;
    background: var(--olive-dark);
    display: flex;
    align-items: center;
    justify-content: flex-end;
    padding-right: 40px;
  }
  .slogan {
    font-weight: 400;
    font-size: 19px;
    letter-spacing: 0.5px;
    color: var(--band-text);
    text-transform: uppercase;
  }
  .person {
    position: absolute;
    right: 150px;
    top: 360px;
    font-size: 34px;
    text-transform: uppercase;
    color: var(--olive-bright);
    line-height: 1;
  }
  .person .first { font-weight: 700; }
  .person .last { font-weight: 400; }
  .contact {
    position: absolute;
    left: 80px;
    right: 40px;
    top: 428px;
    display: flex;
    justify-content: space-between;
    font-size: 22px;
    color: var(--ink);
  }
  .contact .label { font-weight: 700; margin-right: 10px; }
  .contact .value { font-weight: 400; }
</style>
</head>
<body>
  <main class="card">
    <div class="brand">
      <span class="brand-dot"></span>
      <span class="brand-name">Bramble-Wood Yards</span>
    </div>

    <div class="slogan-band">
      <p class="slogan">Complete Gardening &amp; Lawn Maintenance &amp; Horticultural Care</p>
    </div>

    <p class="person"><span class="first">Derek</span> <span class="last">Ostrowe</span></p>

    <div class="contact">
      <p class="contact-item"><span class="label">phone</span><span class="value">0421583906</span></p>
      <p class="contact-item"><span class="label">email</span><span class="value">bramblewoodyards@mailnest.net</span></p>
    </div>
  </main>
</body>
</html>
```